Book Cover design to address Interviewing Skills that lead to job offers

I have written a book about how to interview and get more job offers. Please use primary colors as light or royal blue and yellow. You can creatively add other colors as you like. The final design should convey success.

Title: Quiet Harbors Beyond the Orchard
Other text: Read, apply, repeat

Royal

```html
<!DOCTYPE html>
<html lang="en">
<head>
<meta charset="utf-8">
<title>Quiet Harbors Beyond the Orchard — Book Cover</title>
<link rel="stylesheet" href="https://fonts.googleapis.com/css2?family=Oswald:wght@700&family=Cinzel:wght@700;900&display=swap">
<style>
  :root {
    --cyan: #00ffff;
    --aqua: #3fffc8;
    --lime: #b8ff3c;
    --yellow: #ffff00;
    --title-white: #ffffff;
    --tagline-red: #d3122c;
    --tagline-edge: #7a0a1a;
  }
  html, body {
    margin: 0;
    padding: 0;
    width: 887px;
    height: 1200px;
    overflow: hidden;
  }
  .book-cover {
    position: relative;
    width: 887px;
    height: 1200px;
    overflow: hidden;
    background:
      radial-gradient(ellipse 900px 900px at 887px 545px,
        var(--yellow) 0%,
        var(--lime) 28%,
        var(--aqua) 62%,
        var(--cyan) 92%);
  }
  .cover-heading {
    position: absolute;
    left: 123px;
    top: 112px;
    width: 700px;
    display: flex;
    flex-direction: column;
    align-items: flex-start;
  }
  .cover-title {
    margin: 0;
    font-family: "Oswald", "Arial Narrow", sans-serif;
    font-weight: 700;
    font-size: 80px;
    line-height: 96px;
    letter-spacing: -0.5px;
    text-transform: uppercase;
    color: var(--title-white);
  }
  .cover-tagline {
    margin: 48px 0 0;
    font-family: "Cinzel", Georgia, serif;
    font-weight: 900;
    font-size: 29px;
    line-height: 36px;
    letter-spacing: 0.5px;
    text-transform: uppercase;
    color: var(--tagline-red);
    -webkit-text-stroke: 0.6px var(--tagline-edge);
  }
  .cover-author {
    position: absolute;
    left: 123px;
    top: 1070px;
    margin: 0;
    font-family: "Cinzel", Georgia, serif;
    font-weight: 900;
    font-size: 25px;
    letter-spacing: 0.5px;
    text-transform: uppercase;
    color: var(--title-white);
  }
</style>
</head>
<body>
  <main class="book-cover">
    <header class="cover-heading">
      <h1 class="cover-title">Quiet Harbors Beyond the Orchard</h1>
      <p class="cover-tagline">Read, apply, repeat</p>
    </header>
    <p class="cover-author">Author</p>
  </main>
</body>
</html>
```